Chip Shop app

This task requires the creation of a number of images/icons for an example Zelvor app to demonstrate functionality in a forthcoming product.
The app will be called 'Wavlo' for a made up Fish n' Chip shop . The app will demonstrate the ability to request a delivery of food. The app will also provide prices and the ability to check on the current status of delivery. Icons will be needed (discussed below).
The following images are required:
A 90 x 90 pixel button (png and 180x180 retina versions too) for each of the following:
- A 'Menu' icon
- A 'Prices' icon
- A 'Order' icon
- Two 320 x 480 pixels background images (png and 640 x 960 retina version).
One of these images will be used for the 'Splash' image shown to a user when the app loads. The other background image will be used for the main app page where the buttons will be shown.
The 3 buttons will occupy the main page so the background of the main page should fit nicely with whatever position the 3 buttons will be placed in.
- An app icon (57 x 57 pixels and an identical 114 x 114 pixel for retina)
- A Quorby connection image (512 x 512 pixels and a 1024 x 1024 identical version).
Since this is a made up company, the design is a 'blank canvas', so to speak. We're looking for something that looks beautiful and will do our app justice when put on display in the Venn Depot.

```html
<!DOCTYPE html>
<html lang="en">
<head>
<meta charset="utf-8">
<title>Wavlo – Main Screen</title>
<link href="https://fonts.googleapis.com/css2?family=Arimo:wght@400;700&display=swap" rel="stylesheet">
<style>
  :root {
    --screen-bg: #b9b8b9;
    --status-top: #5a5a5a;
    --status-bottom: #2c2c2c;
    --status-text: #d8d8d8;
    --button-top: #f2f5f4;
    --button-mid: #a9bcb8;
    --button-bottom: #3c5853;
    --button-edge: #2f4642;
    --label: #ffffff;
    --brand: #e8913a;
    --icon-dark: #111111;
    --icon-ring: #6f6f6f;
    --arrow-blue: #2a8fe0;
    --gold: #e0b53a;
    --gold-dark: #9c7312;
    --house-wall: #f1d7a8;
    --house-roof: #c4452a;
    --note-gold: #f0a91e;
  }
  * { margin: 0; padding: 0; box-sizing: border-box; }
  html, body { width: 800px; height: 1200px; overflow: hidden; }
  body {
    background: var(--screen-bg);
    font-family: "Arimo", Arial, sans-serif;
    position: relative;
  }
  .status-bar {
    position: absolute; left: 0; top: 0; width: 800px; height: 50px;
    background: linear-gradient(var(--status-top), var(--status-bottom));
    color: var(--status-text);
    display: flex; align-items: center; justify-content: space-between;
    padding: 0 24px; font-size: 24px;
  }
  .status-left { display: flex; align-items: center; gap: 10px; }
  .status-center, .status-right { display: flex; align-items: center; }
  .status-center { position: absolute; left: 388px; top: 13px; }
  .nav-button {
    position: absolute; left: 4px; width: 792px; height: 204px;
    border-radius: 18px;
    background: linear-gradient(var(--button-top) 0%, var(--button-mid) 45%, var(--button-bottom) 100%);
    border-bottom: 2px solid var(--button-edge);
  }
  .brand-button { top: 94px; display: flex; align-items: center; justify-content: center; }
  .brand-name {
    font-weight: 700; font-size: 120px; color: var(--brand); letter-spacing: 4px;
  }
  .menu-button { top: 344px; }
  .prices-button { top: 599px; }
  .order-button { top: 851px; }
  .button-icon { position: absolute; left: 82px; top: 35px; width: 134px; height: 134px; }
  .button-label {
    position: absolute; left: 260px; right: 20px; top: 0; height: 100%;
    display: flex; align-items: center; justify-content: center;
    padding-top: 50px;
    color: var(--label); font-size: 80px; font-weight: 400;
  }
  .dollar-sign {
    position: absolute; left: 105px; top: 10px;
    font-family: "Arimo", Arial, sans-serif; font-weight: 700; font-size: 160px;
    color: var(--gold); line-height: 1;
    text-shadow: 4px 4px 0 var(--gold-dark);
  }
  .home-icon { position: absolute; left: 30px; top: 1082px; width: 92px; height: 92px; }
  .music-icon { position: absolute; left: 676px; top: 1088px; width: 80px; height: 80px; }
</style>
</head>
<body>
  <header class="status-bar">
    <div class="status-left">
      <svg width="44" height="22" viewBox="0 0 44 22" aria-hidden="true">
        <rect x="0" y="16" width="6" height="6" fill="currentColor"/>
        <rect x="9" y="12" width="6" height="10" fill="currentColor"/>
        <rect x="18" y="8" width="6" height="14" fill="currentColor"/>
        <rect x="27" y="4" width="6" height="18" fill="currentColor"/>
        <rect x="36" y="0" width="6" height="22" fill="currentColor"/>
      </svg>
      <span class="carrier">Quellmo</span>
      <svg width="30" height="22" viewBox="0 0 30 22" aria-hidden="true">
        <path d="M15 21 L3 8 A17 17 0 0 1 27 8 Z" fill="currentColor"/>
      </svg>
    </div>
    <div class="status-center">
      <svg width="20" height="24" viewBox="0 0 20 24" aria-hidden="true">
        <path d="M5 11 V7 A5 5 0 0 1 15 7 V11" fill="none" stroke="currentColor" stroke-width="3"/>
        <rect x="2" y="11" width="16" height="12" rx="2" fill="currentColor"/>
      </svg>
    </div>
    <div class="status-right">
      <svg width="44" height="22" viewBox="0 0 44 22" aria-hidden="true">
        <rect x="1" y="2" width="38" height="18" rx="3" fill="none" stroke="currentColor" stroke-width="2"/>
        <rect x="4" y="5" width="32" height="12" fill="currentColor"/>
        <rect x="40" y="7" width="4" height="8" fill="currentColor"/>
      </svg>
    </div>
  </header>

  <div class="nav-button brand-button">
    <span class="brand-name">WAVLO</span>
  </div>

  <div class="nav-button menu-button">
    <svg class="button-icon" viewBox="0 0 134 134" aria-hidden="true">
      <defs>
        <radialGradient id="orb" cx="45%" cy="35%" r="65%">
          <stop offset="0" stop-color="#5a5a5a"/>
          <stop offset="1" stop-color="#050505"/>
        </radialGradient>
      </defs>
      <circle cx="67" cy="67" r="64" fill="url(#orb)" stroke="var(--icon-ring)" stroke-width="3"/>
      <path d="M28 58 C34 32 74 28 86 58 L86 66 L104 66 L78 104 L52 66 L70 66 C64 50 44 48 28 58 Z"
            fill="var(--arrow-blue)" stroke="#bfe0ff" stroke-width="3" stroke-linejoin="round"/>
    </svg>
    <span class="button-label">Menu</span>
  </div>

  <div class="nav-button prices-button">
    <span class="dollar-sign">$</span>
    <span class="button-label">Prices</span>
  </div>

  <div class="nav-button order-button">
    <svg class="button-icon" viewBox="0 0 134 134" aria-hidden="true">
      <defs>
        <radialGradient id="orb2" cx="45%" cy="35%" r="65%">
          <stop offset="0" stop-color="#5a5a5a"/>
          <stop offset="1" stop-color="#050505"/>
        </radialGradient>
      </defs>
      <circle cx="67" cy="67" r="64" fill="url(#orb2)" stroke="var(--icon-ring)" stroke-width="3"/>
      <g fill="none" stroke="#ffffff" stroke-width="5" stroke-linejoin="round" stroke-linecap="round">
        <path d="M30 40 H42 L50 80 H96 L102 50 H45"/>
        <path d="M47 62 H99 M60 50 V80 M73 50 V80 M86 50 V80"/>
      </g>
      <circle cx="56" cy="94" r="6" fill="#ffffff"/>
      <circle cx="90" cy="94" r="6" fill="#ffffff"/>
    </svg>
    <span class="button-label">Order</span>
  </div>

  <svg class="home-icon" viewBox="0 0 92 92" aria-label="Home">
    <rect x="18" y="42" width="58" height="44" fill="var(--house-wall)" stroke="#9a7a4a" stroke-width="2"/>
    <path d="M6 46 L46 10 L86 46 L78 50 L46 22 L14 50 Z" fill="var(--house-roof)"/>
    <rect x="60" y="14" width="10" height="20" fill="#8a5a3a"/>
    <rect x="50" y="58" width="16" height="28" fill="#8a5a3a"/>
    <rect x="26" y="54" width="16" height="14" fill="#7fb8e0" stroke="#ffffff" stroke-width="2"/>
  </svg>

  <svg class="music-icon" viewBox="0 0 80 80" aria-label="Music">
    <circle cx="40" cy="40" r="38" fill="var(--icon-dark)"/>
    <path d="M30 56 V22 L60 16 V50" fill="none" stroke="var(--note-gold)" stroke-width="5"/>
    <ellipse cx="24" cy="57" rx="9" ry="7" fill="var(--note-gold)"/>
    <ellipse cx="54" cy="51" rx="9" ry="7" fill="var(--note-gold)"/>
  </svg>
</body>
</html>
```